Allied Health Clinic needs catchy poster ad for lightbox

We need a catchy and effective poster designed for our retail lightbox which is in a busy corridor. We are a multi disciplinary sports injury clinic offering a range of allied health services. Established in 1999. We need people to understand our business identity and services clearly. I have come up with a very rough idea as far as what I think the copy should contain. The picture is an example of what image I am trying to convey to the potential client. I am not a designer clearly. We specialise in treating difficult problems.
Size of the poster is 451mm x 741mm at 300dpi. We will then blow the image up to double this size which will be good enough resolution for the printing.

Target Market(s)

White collar professionals - male and female, active 20-50 range

Industry/Entity Type

Healthcare

Font styles to use
Sans Serif

Requirements
Nice to have
• Easy to read, polished, nice tie in to my logo colours

```html
<!DOCTYPE html>
<html lang="en">
<head>
<meta charset="utf-8">
<title>Injury Experts – Corefit Physiotherapy</title>
<link rel="stylesheet" href="https://fonts.googleapis.com/css2?family=Montserrat:wght@400;500;700;800;900&display=swap">
<style>
  :root {
    --white: #ffffff;
    --ink: #232323;
    --headline-light: #ece9f3;
    --green-bright: #4fd835;
    --green-deep: #2f8f3a;
    --olive: #3f5a1f;
    --logo-green: #8cc63f;
    --logo-grey: #4a4a4a;
    --bar: #2a2a2a;
    --sky-dark: #262c3a;
    --sky-mid: #5b5660;
    --sun: #f4d9a6;
    --pitch: #3e6b2c;
  }
  * { margin: 0; padding: 0; box-sizing: border-box; }
  html, body { width: 730px; height: 1200px; overflow: hidden; background: var(--white); }
  .poster {
    position: relative;
    width: 730px;
    height: 1200px;
    overflow: hidden;
    background: var(--white);
    font-family: "Montserrat", Arial, sans-serif;
    color: var(--ink);
  }
  .hero-photo {
    position: absolute;
    left: 0; top: 0;
    width: 730px; height: 890px;
    background:
      linear-gradient(to bottom, rgba(255,255,255,0) 0%, rgba(255,255,255,0) 72%, rgba(255,255,255,0.85) 88%, #fff 100%),
      radial-gradient(ellipse 260px 170px at 240px 390px, rgba(255,244,220,0.95) 0%, rgba(244,217,166,0.6) 40%, rgba(244,217,166,0) 100%),
      linear-gradient(to bottom, transparent 0%, transparent 60%, #5c4a45 66%, #6b5450 72%, var(--pitch) 78%, #557f3d 86%),
      linear-gradient(to bottom, var(--sky-dark) 0%, #3a3f4d 20%, var(--sky-mid) 40%, #9a8270 55%, #7a6560 62%);
  }
  .headline {
    position: absolute;
    left: 40px;
    top: 22px;
    font-weight: 900;
    line-height: 1;
  }
  .headline-injury {
    display: block;
    font-size: 152px;
    letter-spacing: -2px;
    color: var(--headline-light);
  }
  .headline-experts {
    display: block;
    margin-top: -2px;
    font-size: 100px;
    font-weight: 900;
    letter-spacing: -1px;
    background: linear-gradient(to right, var(--green-bright) 0%, var(--green-bright) 55%, var(--green-deep) 100%);
    -webkit-background-clip: text;
    background-clip: text;
    color: transparent;
  }
  .tagline {
    position: absolute;
    left: 43px;
    top: 278px;
    font-size: 45px;
    font-weight: 800;
    line-height: 1.02;
    color: var(--ink);
  }
  .track-record {
    position: absolute;
    left: 42px;
    top: 632px;
    font-size: 24px;
    font-weight: 500;
    line-height: 34px;
    color: var(--ink);
  }
  .track-record strong { font-weight: 800; }
  .services {
    position: absolute;
    left: 42px;
    top: 788px;
  }
  .services-intro {
    font-size: 23px;
    font-weight: 500;
    color: var(--ink);
    margin-bottom: 10px;
  }
  .services-list {
    font-size: 24px;
    font-weight: 800;
    line-height: 33px;
    color: var(--olive);
  }
  .services-list .divider { font-weight: 400; color: var(--ink); margin: 0 4px; }
  .brand {
    position: absolute;
    left: 70px;
    top: 966px;
    display: flex;
    align-items: center;
    gap: 28px;
  }
  .brand-dot {
    width: 90px; height: 90px;
    border-radius: 50%;
    background: var(--logo-green);
    flex: none;
  }
  .brand-name {
    font-size: 30px;
    font-weight: 500;
    line-height: 1.2;
    color: var(--logo-grey);
  }
  .directions {
    position: absolute;
    left: 0; right: 0;
    top: 1094px;
    text-align: center;
    font-size: 25px;
    font-weight: 500;
    color: var(--ink);
  }
  .directions .level {
    background: var(--bar);
    color: var(--white);
    padding: 0 6px;
  }
  .contact-bar {
    position: absolute;
    left: 0; bottom: 0;
    width: 730px; height: 62px;
    background: var(--bar);
    color: var(--white);
    display: flex;
    align-items: center;
    justify-content: center;
    gap: 16px;
    font-size: 24px;
    font-weight: 500;
  }
  .contact-item { display: flex; align-items: center; gap: 6px; }
  .contact-item svg { width: 20px; height: 20px; fill: none; stroke: var(--white); }
</style>
</head>
<body>
<div class="poster">
  <div class="hero-photo" role="img" aria-label="Footballer in a dark kit striking a ball in a floodlit stadium under a stormy sky, with glowing red highlights on elbow and knees"></div>

  <h1 class="headline">
    <span class="headline-injury">INJURY</span>
    <span class="headline-experts">EXPERTS</span>
  </h1>

  <p class="tagline">TRUSTED BY<br>ATHLETES</p>

  <p class="track-record">SUCCESSFULLY TREATING<br>DIFFICULT INJURIES<br><strong>SINCE 1999</strong></p>

  <div class="services">
    <p class="services-intro">A Complete range of services</p>
    <p class="services-list">SPORTS PHYSIOTHERAPY<span class="divider">|</span>CHIROPRACTIC<br>MASSAGE<span class="divider">|</span>PODIATRY<span class="divider">|</span>EXERCISE PHYSIOLOGY</p>
  </div>

  <div class="brand">
    <span class="brand-dot"></span>
    <p class="brand-name">Corefit Physiotherapy<br>&amp; Sports Injury Clinic</p>
  </div>

  <p class="directions">TAKE LIFTS TO <span class="level">LEVEL 8</span></p>

  <div class="contact-bar">
    <span class="contact-item">
      <svg viewBox="0 0 24 24" aria-hidden="true"><path d="M5 3h4l2 5-2.5 1.5a11 11 0 0 0 6 6L16 13l5 2v4a2 2 0 0 1-2 2A16 16 0 0 1 3 5a2 2 0 0 1 2-2z" fill="#fff" stroke="none"/></svg>
      8123 4567
    </span>
    <span class="contact-item">
      <svg viewBox="0 0 24 24" aria-hidden="true" stroke-width="1.8"><circle cx="12" cy="12" r="9"/><ellipse cx="12" cy="12" rx="4" ry="9"/><path d="M3 12h18M5 7h14M5 17h14"/></svg>
      corefitphysioclinic.com.au
    </span>
  </div>
</div>
</body>
</html>
```